Web design project for exciting Australian start-up

Background
We are looking for a creative and talented web design artist to work alongside our market leading web developer.
• You will be required to create a modern and clean design theme for our website, incorporating selected rustic colour scheme elements for our exciting Australian start-up to operate within the coffee industry.
reoccurring work to be expected to flow to the successful designer.
Requirements
• c. 5 - 10 page website
• Landing page
• Log in/ out
• 404 template
• Typography is emphasised
• Please use either a) typevane.com, b) free web fonts, c) marlo fonts
• All design elements in vector format
• Preferably with icons for each header title(i.e. about us, how it works etc) but designer have free reign over how the site looks, so might not be applicable
• All pages to be responsive
• Down to iPad resolution

High level visual design brief attached - additional pages to be worked from base design.

Design inspiration
• We would like to use design elements from the following sources:
http://www.brivantel.com/sorvik/ (Functionality)
Colour scheme refer to logo and complementary style guide
Updates

```html
<!DOCTYPE html>
<html lang="en">
<head>
<meta charset="utf-8">
<title>Brewhaven – Australia's First Online Coffee Marketplace</title>
<link rel="stylesheet" href="https://fonts.googleapis.com/css2?family=League+Gothic&family=Oswald:wght@400;600&display=swap">
<style>
  :root {
    --white: #ffffff;
    --ink: #2b2622;
    --orange: #e8873a;
    --espresso: #24170f;
    --tan: #c9a878;
    --icon-tone: #efe4d8;
    --rule: #cfcac4;
    --hero-dark: #5a3b22;
    --hero-mid: #a7845f;
    --hero-light: #dcc8ab;
  }
  * { box-sizing: border-box; margin: 0; padding: 0; }
  html, body {
    width: 1200px; height: 901px; overflow: hidden;
    background: var(--white);
    font-family: "League Gothic", "Oswald", sans-serif;
  }
  .page { position: relative; width: 1200px; height: 901px; }

  /* Header */
  .site-header {
    position: absolute; left: 0; top: 0; width: 1200px; height: 157px;
    background: var(--white);
    border-bottom: 3px solid var(--rule);
  }
  .brand {
    position: absolute; left: 21px; top: 42px;
    display: flex; align-items: center; gap: 14px;
    font-family: "Oswald", sans-serif; font-weight: 600;
    font-size: 38px; letter-spacing: 2px; color: var(--ink);
    text-decoration: none;
  }
  .brand-dot {
    width: 48px; height: 48px; border-radius: 50%;
    background: var(--orange);
  }
  .main-nav {
    position: absolute; top: 12px; left: 500px; right: 10px;
    display: flex; justify-content: space-between;
  }
  .nav-item {
    width: 170px; display: flex; flex-direction: column; align-items: center;
    text-decoration: none; color: var(--orange);
  }
  .nav-icon {
    width: 90px; height: 86px; border-radius: 8px;
    background: var(--icon-tone);
  }
  .nav-label {
    margin-top: 10px; font-size: 36px; line-height: 1; letter-spacing: 0.5px;
  }

  /* Hero */
  .hero {
    position: absolute; left: 0; top: 160px; width: 1200px; height: 630px;
    overflow: hidden;
  }
  .hero-photo {
    position: absolute; inset: 0;
    background:
      radial-gradient(ellipse 340px 300px at 860px 330px, #f3efe9 0%, #e9e1d5 55%, rgba(233,225,213,0) 100%),
      linear-gradient(100deg, var(--hero-dark) 0%, var(--hero-mid) 38%, var(--hero-light) 68%, var(--hero-mid) 100%);
  }
  .hero-title {
    position: absolute; left: 80px; top: 90px;
    color: var(--white); font-weight: 400; line-height: 0.9;
    text-shadow: 0 1px 6px rgba(40, 25, 15, 0.35);
  }
  .hero-title .line-small { display: block; font-size: 78px; letter-spacing: 0.5px; }
  .hero-title .line-large { display: block; font-size: 92px; letter-spacing: 1.5px; }
  .watch-video {
    position: absolute; left: 77px; top: 431px; width: 391px; height: 97px;
    border-radius: 7px; background: rgba(36, 23, 15, 0.92);
    display: flex; align-items: center; gap: 30px; padding-left: 24px;
    color: var(--tan); text-decoration: none;
    font-size: 56px; line-height: 1;
  }
  .watch-video svg { flex: none; }

  /* Footer */
  .site-footer {
    position: absolute; left: 0; top: 790px; width: 1200px; height: 111px;
    background: var(--espresso);
    border-top: 3px solid var(--white);
  }
  .copyright {
    position: absolute; left: 34px; top: 38px;
    font-size: 28px; color: var(--tan); letter-spacing: 0.3px;
  }
  .footer-brand {
    position: absolute; right: 34px; top: 26px;
    display: flex; align-items: center; gap: 12px;
    font-family: "Oswald", sans-serif; font-weight: 600;
    font-size: 30px; letter-spacing: 2px; color: var(--white);
  }
  .footer-brand .brand-dot { width: 42px; height: 42px; background: #8d8a86; }
</style>
</head>
<body>
<div class="page">
  <header class="site-header">
    <a class="brand" href="#"><span class="brand-dot"></span>BREWHAVEN</a>
    <nav class="main-nav">
      <a class="nav-item" href="#">
        <span class="nav-icon" role="img" aria-label="Sketched coffee cup illustration"></span>
        <span class="nav-label">HELPFUL INFO</span>
      </a>
      <a class="nav-item" href="#">
        <span class="nav-icon" role="img" aria-label="Sketched coffee grinder illustration"></span>
        <span class="nav-label">WHO WE ARE</span>
      </a>
      <a class="nav-item" href="#">
        <span class="nav-icon" role="img" aria-label="Sketched espresso machine illustration"></span>
        <span class="nav-label">JOIN US</span>
      </a>
      <a class="nav-item" href="#">
        <span class="nav-icon" role="img" aria-label="Sketched coffee bag illustration"></span>
        <span class="nav-label">REGISTER</span>
      </a>
    </nav>
  </header>

  <section class="hero">
    <div class="hero-photo" role="img" aria-label="Photo of a steaming white coffee cup on a saucer beside a burlap sack of spilled coffee beans on a wooden table"></div>
    <h1 class="hero-title">
      <span class="line-small">AUSTRALIA’S</span>
      <span class="line-small">FIRST ONLINE</span>
      <span class="line-large">COFFEE</span>
      <span class="line-large">MARKETPLACE</span>
    </h1>
    <a class="watch-video" href="#">
      <svg width="58" height="58" viewBox="0 0 58 58" aria-hidden="true">
        <circle cx="29" cy="29" r="28" fill="#c9a878"/>
        <path d="M22 16 L41 29 L22 42 Z" fill="#24170f"/>
      </svg>
      <span>WATCH VIDEO</span>
    </a>
  </section>

  <footer class="site-footer">
    <p class="copyright">COPYRIGHT © 2014 BREWHAVEN</p>
    <div class="footer-brand"><span class="brand-dot"></span>BREWHAVEN</div>
  </footer>
</div>
</body>
</html>
```